Rollaway Stays

We are 100% online, promoting accommodation details and booking facilities for wheelchair dependant travellers.
Listings will only be accommodation providers which meet our specific criteria.

Target Market(s)

Wheelchair dependant people and their companions

Industry/Entity Type

Accommodation

Contact Information for Business Card

Name, mobile phone number, email address, website address

```html
<!DOCTYPE html>
<html lang="en">
<head>
<meta charset="utf-8">
<title>Rollaway Stays – Business Card</title>
<link href="https://fonts.googleapis.com/css2?family=Lato:wght@400;700;900&display=swap" rel="stylesheet">
<style>
  :root {
    --bg: #2a2a2a;
    --card-white: #ffffff;
    --brand-red: #e5202a;
    --card-black: #050505;
    --text-light: #ffffff;
  }
  * { margin: 0; padding: 0; box-sizing: border-box; }
  html, body {
    width: 1200px;
    height: 1000px;
    overflow: hidden;
    background: var(--bg);
    font-family: 'Lato', sans-serif;
  }
  .stage {
    position: relative;
    width: 1200px;
    height: 1000px;
  }
  .business-card {
    position: absolute;
    left: 150px;
    top: 243px;
    width: 900px;
    height: 514px;
    border-radius: 24px;
    overflow: hidden;
    background: var(--card-black);
  }
  .card-top {
    position: absolute;
    left: 0; top: 0;
    width: 100%;
    height: 292px;
    background: var(--card-white);
    border-bottom: 9px solid var(--brand-red);
  }
  .brand {
    position: absolute;
    left: 58px;
    top: 110px;
    display: flex;
    align-items: center;
    gap: 18px;
  }
  .brand-dot {
    width: 46px;
    height: 46px;
    border-radius: 50%;
    background: var(--brand-red);
  }
  .brand-name {
    font-weight: 900;
    font-size: 58px;
    color: var(--brand-red);
    letter-spacing: -0.5px;
  }
  .person-name {
    position: absolute;
    left: 560px;
    top: 72px;
    font-weight: 700;
    font-size: 30px;
    color: var(--brand-red);
  }
  .contact-list {
    position: absolute;
    left: 66px;
    top: 332px;
    list-style: none;
  }
  .contact-item {
    display: flex;
    align-items: center;
    gap: 22px;
    height: 50px;
    color: var(--text-light);
    font-size: 28px;
    font-weight: 400;
    letter-spacing: 0.5px;
  }
  .contact-icon {
    width: 38px;
    height: 38px;
    flex-shrink: 0;
  }
</style>
</head>
<body>
<main class="stage">
  <article class="business-card">
    <section class="card-top">
      <div class="brand">
        <span class="brand-dot"></span>
        <span class="brand-name">Rollaway Stays</span>
      </div>
      <p class="person-name">Daniel Harcourt</p>
    </section>

    <ul class="contact-list">
      <li class="contact-item">
        <svg class="contact-icon" viewBox="0 0 38 38" aria-hidden="true">
          <circle cx="19" cy="19" r="19" fill="var(--brand-red)"/>
          <path d="M13 10 l4 0 l2 5 l-3 2 a12 12 0 0 0 6 6 l2 -3 l5 2 l0 4 a2 2 0 0 1 -2 2 a18 18 0 0 1 -16 -16 a2 2 0 0 1 2 -2z" fill="#fff"/>
        </svg>
        <span>[+61] 0400 123 456</span>
      </li>
      <li class="contact-item">
        <svg class="contact-icon" viewBox="0 0 38 38" aria-hidden="true">
          <circle cx="19" cy="19" r="19" fill="var(--brand-red)"/>
          <rect x="9" y="12" width="20" height="14" rx="1.5" fill="#fff"/>
          <path d="M9.5 12.5 L19 20 L28.5 12.5" fill="none" stroke="var(--brand-red)" stroke-width="1.6"/>
        </svg>
        <span>hello@rollawaystays.com.au</span>
      </li>
      <li class="contact-item">
        <svg class="contact-icon" viewBox="0 0 38 38" aria-hidden="true">
          <circle cx="19" cy="19" r="19" fill="var(--brand-red)"/>
          <g fill="none" stroke="#fff" stroke-width="1.6">
            <circle cx="19" cy="19" r="9"/>
            <ellipse cx="19" cy="19" rx="4" ry="9"/>
            <line x1="10" y1="19" x2="28" y2="19"/>
            <line x1="11.5" y1="14" x2="26.5" y2="14"/>
            <line x1="11.5" y1="24" x2="26.5" y2="24"/>
          </g>
        </svg>
        <span>www.rollawaystays.com.au</span>
      </li>
    </ul>
  </article>
</main>
</body>
</html>
```